Modern Small Law Firm Website To Look Cutting Edge

I need a website design for a new, single-attorney law firm. The firm will be called "The Thornwell Law Group." Our goal is to handle car accident and general personal injury lawsuits for individuals.

Our selling points are: (1) We charge less so you keep more; (2) We have experience and success trying and settling multi-million dollar cases; (3) We use modern technology to make the whole process simple, easy and hassle-free for clients.

Also because we are a one-man law firm, the clients will personally know the lawyer and have access to them. For that reason, I thought a good big tagline for the website would be "KNOW YOUR LAWYER"

I like the idea of splitting the website vertically down the middle, with the left side having a blue background, a picture of me, and big white lettering for the tagline, and the right side having a white background with blue lettering and headlines. I don't want navy blue or royal blue, but a more bright and eye-catching blue color. We can experiment with different shades.

I would be curious about how it could look with some minor orange accent coloring somewhere.

I need to feature prominently, probably in the top left corner, this phone number: 504-917-2083.

This will be used as much by mobile users as it would be by desktop/computer users.

The final design should communicate trust, convenience and cutting edge technology that leads to success.

Finally, I would be curious how we can have a sleek looking info submission box somewhere on the right side nearer the bottom that features different combinations of presenting these phrases: "QUICK QUESTION? QUICK ANSWER" The info submission button could say "Ask"

I am uploading two different pictures of me that can be used. The gray backgrounds are not necessary or good, if there is a way to cut them out that would be great. I can try and get that if needed.

Target Market(s)

Individuals who have been hurt by others, mostly in car accidents. They will be frustrated, inconvenienced and need to be soothed.

Industry/Entity Type

Legal

Number of Pages Required

1 page

Font styles to use
Sans Serif

Colors
0692cd
33a6d7
85cae6
faa54b
f78f20
3276b5

Requirements
Must have
• If you have started designing already, please note that the project description information is more important than the image that I uploaded originally. It has since been deleted.
• Also please now use the color photo that has been uploaded.
Nice to have
• I really want a clean and simple website design with not a lot of clutter. I'd like to avoid the typical law firm websites that you see that have tool bars across the top and basic borders/columns everywhere. It needs to grab your attention and look a little more cutting edge and different.
• Let's experiment with different eye-catching ways to present the three value propositions I noted.
• Also if the screen is split vertically with the left and right side being blue and white, maybe we can experiment with different ways that the two colors could fade into each other as opposed to just a line where one color starts and the other ends.
• And maybe the blue/white backgrounds could be textured somehow so that they don't appear flat. Perhaps we could try using differing shades of blue to give the appearance of pattern or 3D texture.
Should not have
• The basic picture/design I uploaded is just a suggestion, but there isn't really anything there.

```html
<!DOCTYPE html>
<html lang="en">
<head>
<meta charset="utf-8">
<title>The Thornwell Law Group</title>
<link rel="stylesheet" href="https://fonts.googleapis.com/css2?family=Libre+Baskerville&family=Raleway:wght@300;400&family=Open+Sans:wght@400&display=swap">
<style>
  :root {
    --blue: #0692cd;
    --blue-mid: #33a6d7;
    --blue-light: #85cae6;
    --blue-bright: #3db0e3;
    --orange: #f78f20;
    --orange-soft: #faa54b;
    --dot-gold: #e3b51b;
    --ink: #222;
    --grey-text: #666;
    --grey-logo: #777;
    --form-bg: #efefef;
    --field-border: #d4d4d4;
    --footer-bg: #2b2b2b;
    --footer-text: #d0d0d0;
    --footer-muted: #a8a8a8;
    --white: #fff;
  }
  * { margin: 0; padding: 0; box-sizing: border-box; }
  html, body { width: 1091px; height: 1200px; overflow: hidden; background: var(--white); }
  .page { position: relative; width: 1091px; height: 1200px; font-family: "Open Sans", sans-serif; color: var(--ink); }

  .site-header { position: absolute; left: 0; top: 0; width: 1091px; height: 112px; background: var(--white); }
  .header-phone { position: absolute; left: 120px; top: 49px; display: flex; align-items: center; gap: 8px; font-size: 20px; color: #333; letter-spacing: .3px; }
  .header-phone svg { display: block; }
  .brand { position: absolute; left: 0; width: 1091px; top: 28px; text-align: center; font-family: "Libre Baskerville", serif; color: var(--blue); line-height: 1; }
  .brand-main { display: block; font-size: 30px; letter-spacing: .5px; }
  .brand-sub { display: block; font-size: 21px; margin-top: 7px; letter-spacing: 1px; }
  .menu-toggle { position: absolute; left: 912px; top: 51px; width: 40px; }
  .menu-toggle span { display: block; height: 3px; background: #b5b5b5; margin-bottom: 5px; }

  .hero { position: absolute; left: 0; top: 112px; width: 1091px; height: 505px; }
  .hero-photo { position: absolute; inset: 0; background: linear-gradient(100deg, #4d87b6 0%, #5a7fa0 30%, #465a78 55%, #5a6a84 75%, #6a7896 100%); }
  .hero-photo::after { content: ""; position: absolute; inset: 0; background: linear-gradient(180deg, rgba(120,120,90,.35) 0%, rgba(0,0,0,0) 25%, rgba(30,30,35,.35) 100%); }
  .hero-title { position: absolute; left: 0; width: 1070px; top: 170px; text-align: center; font-family: "Libre Baskerville", serif; color: var(--white); font-size: 50px; letter-spacing: 1px; line-height: 1; }
  .hero-sub { position: absolute; left: 0; width: 1070px; top: 238px; text-align: center; font-family: "Libre Baskerville", serif; color: var(--white); font-size: 26px; letter-spacing: .5px; }
  .slider-dots { position: absolute; left: 510px; top: 471px; display: flex; gap: 4px; }
  .slider-dots span { width: 16px; height: 16px; border-radius: 50%; background: var(--white); }
  .slider-dots .is-active { background: var(--dot-gold); border: 2px solid var(--white); }

  .intro-panel { position: absolute; left: 0; top: 617px; width: 548px; height: 478px; background: linear-gradient(160deg, var(--blue-bright) 0%, var(--blue-mid) 45%, var(--blue) 100%); overflow: hidden; color: var(--white); }
  .attorney-photo { position: absolute; left: 300px; top: 14px; width: 248px; height: 464px; background: linear-gradient(180deg, rgba(60,70,90,.25) 0%, #2a2c35 45%, #1c1d24 100%); border-radius: 120px 120px 0 0; }
  .intro-title { position: absolute; left: 113px; top: 68px; font-family: "Raleway", sans-serif; font-weight: 300; font-size: 43px; line-height: 1; letter-spacing: 1px; }
  .intro-subtitle { position: absolute; left: 113px; top: 120px; font-family: "Raleway", sans-serif; font-weight: 300; font-size: 27px; letter-spacing: 1px; }
  .intro-lead { position: absolute; left: 115px; top: 165px; width: 220px; font-size: 13.5px; line-height: 21px; }
  .intro-body { position: absolute; left: 115px; top: 218px; width: 200px; font-size: 11.5px; line-height: 20.5px; }
  .btn-outline { position: absolute; left: 118px; top: 940px; }
  .intro-cta { position: absolute; left: 118px; top: 323px; width: 116px; height: 36px; border: 2px solid var(--white); display: flex; align-items: center; justify-content: center; font-family: "Raleway", sans-serif; font-size: 13.5px; letter-spacing: .5px; color: var(--white); }

  .benefits { position: absolute; left: 548px; top: 617px; width: 543px; height: 283px; background: var(--white); }
  .benefit { position: absolute; left: 39px; width: 420px; }
  .benefit-icon { position: absolute; left: 0; top: 0; width: 68px; height: 68px; }
  .benefit-title { position: absolute; left: 123px; font-family: "Raleway", sans-serif; font-size: 15.5px; color: #111; letter-spacing: .3px; white-space: nowrap; }
  .benefit-text { position: absolute; left: 124px; width: 250px; font-size: 12px; line-height: 16.5px; color: var(--grey-text); }

  .quick-form { position: absolute; left: 548px; top: 900px; width: 543px; height: 195px; background: var(--form-bg); }
  .quick-form h2 { position: absolute; left: 40px; top: 21px; font-family: "Raleway", sans-serif; font-weight: 400; font-size: 15.5px; color: #111; letter-spacing: .2px; }
  .field { position: absolute; background: var(--white); border: 1px solid var(--field-border); font-size: 11px; color: var(--grey-text); padding: 8px 11px; }
  .btn-ask { position: absolute; left: 40px; top: 146px; width: 76px; height: 30px; background: var(--orange); color: var(--white); font-family: "Open Sans", sans-serif; font-size: 16px; display: flex; align-items: center; justify-content: center; }

  .site-footer { position: absolute; left: 0; top: 1095px; width: 1091px; height: 105px; background: var(--footer-bg); }
  .footer-nav { position: absolute; left: 118px; top: 26px; display: flex; gap: 20px; font-family: "Raleway", sans-serif; font-size: 14.5px; color: var(--footer-text); }
  .footer-legal { position: absolute; left: 118px; top: 58px; font-size: 11px; color: var(--footer-muted); }
  .social-links { position: absolute; left: 852px; top: 23px; display: flex; gap: 3px; }
  .social-links span { width: 28px; height: 28px; border: 1.5px solid var(--white); border-radius: 50%; }
</style>
</head>
<body>
<div class="page">

  <header class="site-header">
    <div class="header-phone">
      <svg width="28" height="28" viewBox="0 0 28 28" aria-hidden="true">
        <circle cx="14" cy="14" r="14" fill="#f7a21b"/>
        <path d="M10 8.5c-1 .6-1.6 1.6-1.2 3 .9 3.3 3.5 6.1 6.8 7.3 1.3.5 2.4 0 3.1-1l-2.2-2.1-1.4.9c-1.3-.7-2.4-1.8-3.1-3.1l.9-1.4z" fill="none" stroke="#fff" stroke-width="1.6" stroke-linejoin="round"/>
      </svg>
      <span>504-917-2083</span>
    </div>
    <div class="brand">
      <span class="brand-main">THE THORNWELL</span>
      <span class="brand-sub">LAW GROUP</span>
    </div>
    <div class="menu-toggle" aria-label="Menu"><span></span><span></span><span></span></div>
  </header>

  <section class="hero">
    <div class="hero-photo" role="img" aria-label="Photo of a young man on the phone sitting beside two cars after a collision"></div>
    <h1 class="hero-title">KNOW YOUR LAWYER</h1>
    <p class="hero-sub">FUSCE ULTRICIES ORCI FEUGIAT</p>
    <div class="slider-dots"><span class="is-active"></span><span></span><span></span><span></span></div>
  </section>

  <section class="intro-panel">
    <div class="attorney-photo" role="img" aria-label="Portrait of the attorney in a dark suit and striped tie"></div>
    <h2 class="intro-title">CAR WREK</h2>
    <p class="intro-subtitle">CAN WE HELP</p>
    <p class="intro-lead">Fusce ultricies orci ac feugiat suscipit leo massa</p>
    <p class="intro-body">scelerisque mi tortor at ipsum cligula augue bibendum accumsan vestibulum ut enatis nec euismod sit amet egras id elit Integer</p>
    <a class="intro-cta">CLICK HERE</a>
  </section>

  <section class="benefits">
    <div class="benefit" style="top:35px">
      <svg class="benefit-icon" viewBox="0 0 68 68" aria-hidden="true">
        <circle cx="34" cy="34" r="34" fill="var(--blue-bright)"/>
        <path d="M29 20h10l-3 5h-4z" fill="#fff"/>
        <path d="M31 26h6c6 4 9 9 9 14 0 5-4 8-12 8s-12-3-12-8c0-5 3-10 9-14z" fill="#fff"/>
        <text x="34" y="44" text-anchor="middle" font-family="Open Sans, sans-serif" font-size="13" fill="var(--blue-bright)">$</text>
      </svg>
      <div class="benefit-title" style="top:11px">NEVER MORE THEN 24%</div>
      <p class="benefit-text" style="top:36px">Our lawyers will never overcharge you like others well</p>
    </div>
    <div class="benefit" style="top:118px">
      <svg class="benefit-icon" viewBox="0 0 68 68" aria-hidden="true">
        <circle cx="34" cy="34" r="34" fill="var(--blue-bright)"/>
        <circle cx="34" cy="34" r="19" fill="none" stroke="#fff" stroke-width="4"/>
        <circle cx="34" cy="34" r="5" fill="#fff"/>
        <g stroke="#fff" stroke-width="4">
          <line x1="34" y1="15" x2="34" y2="29"/>
          <line x1="16" y1="29" x2="29" y2="33"/>
          <line x1="52" y1="29" x2="39" y2="33"/>
          <line x1="23" y1="49" x2="31" y2="38"/>
          <line x1="45" y1="49" x2="37" y2="38"/>
        </g>
      </svg>
      <div class="benefit-title" style="top:12px">WE MAKE IT EASY</div>
      <p class="benefit-text" style="top:37px">These new brake pads are really cool, you won't believe it</p>
    </div>
    <div class="benefit" style="top:201px">
      <svg class="benefit-icon" viewBox="0 0 68 68" aria-hidden="true">
        <circle cx="34" cy="34" r="34" fill="var(--blue-bright)"/>
        <g stroke="#fff" stroke-width="2.5" fill="none">
          <line x1="34" y1="18" x2="34" y2="48"/>
          <line x1="19" y1="24" x2="49" y2="24"/>
          <line x1="26" y1="49" x2="42" y2="49"/>
          <path d="M19 24l-6 14h12z M49 24l-6 14h12z"/>
        </g>
        <path d="M13 38h12a6 4 0 0 1-12 0zM43 38h12a6 4 0 0 1-12 0z" fill="#fff"/>
      </svg>
      <div class="benefit-title" style="top:12px">BIG FIRM LAWYERING</div>
      <p class="benefit-text" style="top:37px">With expereince in multi-million dollar litigation, we're the best</p>
    </div>
  </section>

  <section class="quick-form">
    <h2>QUICK QUESTION? QUICK ANSWER</h2>
    <div class="field" style="left:40px;top:48px;width:125px;height:28px">Name</div>
    <div class="field" style="left:169px;top:48px;width:125px;height:28px">Email address</div>
    <div class="field" style="left:302px;top:48px;width:125px;height:28px">Phone</div>
    <div class="field" style="left:40px;top:82px;width:387px;height:60px">Message</div>
    <a class="btn-ask">Ask</a>
  </section>

  <footer class="site-footer">
    <nav class="footer-nav">
      <span>Home</span><span>About Us</span><span>Law Services</span><span>Ask Us</span><span>Resources</span><span>Contact</span>
    </nav>
    <p class="footer-legal">© 2016 Company Name &nbsp;All right reserved &nbsp;Term of Use</p>
    <div class="social-links" aria-label="Social links"><span></span><span></span><span></span><span></span></div>
  </footer>

</div>
</body>
</html>
```